Packaged Food Business Needs a Packaging Design

We need a package design to be used as a label/sticker on the lids of round and square transparent plastic containers and on the sides of resealable stand-up pouches. The brand name is 'Savourly' - please find attached logo together with pictures of the sample containers and pouch. We will use the packaging to market a wide variety of food categories from nuts, dried fruits, spices, cooking chocolates, baking ingredients, cereals, grains and pulses.

OVERALL FEEDBACK ON DESIGNS ALREADY RECEIVED:

- We have found so far that a lot of our mandatory requirements are not adhered to in designs that have been submitted so far. We would like to emphasise that the ingredient, weight and expiry text will be printed at the time of packing so it should not take prime space on the pack BUT at the same time some 'blank' space needs to flawlessly be incorporated into the overall design for this purpose
- We encourage you to glorify the brand logo in the pack, and absolutely refrain from duplicating the tagline
- Please note that ONE label design will be used to pack a wide variety of food ingredients and therefore please ensure that the choice of your design incorporates this requirement, in the past we have received designs that are limited to only one type of food (like nuts) or have received designs that are too floral or leafy (and not grounded to food
- Please ensure that you submit designs for all three packaging formats, it is critical to see the family look from the on-set

Target Market(s)

The brand is targeting both mothers and professional chefs and therefore the label design should be broadly approachable and convey affordable premium

Industry/Entity Type

Business

Requirements
Must have
• - Consistent with the brand name and logo, the overall look and feel of the packaging should convey values of healthy, gourmet food ingredients, high in nourishment and project a sense of delightful taste
• - The design styling to be modern and 'simplistic' (embracing 'less-is-more' type of a design style)
• - Design a packaging architecture that incorporates the brand logo together with its tagline lock-up of 'taste the goodness in every spoonful' - find logo attached
• - The design needs to have a dedicated area to print the ingredient (e.g., Mixed Nuts), weight (e.g., 500g) and expiry (this space needs to be flawlessly incorporated into the design) - this information will be printed either with an inkjet printer or with a rubber stamp so please leave an empty space (the text should not be part of the design, just the area for the text needs to be included in the design)
• - The packaging must include 'Packed By: Mwenda Traders Ltd, P. O. Box 41562, Kampala - Uganda'
• - For the design of the resealable pouch, please incorporate a window to see through the ingredients and a hole on top to hang on supermarket pegs if necessary
Nice to have
• - We would love to have some design submissions that are bold and cheerful and fun (but not frivolous) - please see attached inspiration for 'fun' packaging. The attachments are purely for inspiration, not to infringe on anyone else's TM and copyrights
• - Incorporate green to convey healthy, organic values
• - Explore use of gold and silver convey premiumness
Should not have
• - Do not duplicate the tagline
• - Do not include the ingredient, weight and expiry in the main graphic of the design, these will be printed at the time of packing so ensure there is provision for this in a flawless way in the design (e.g., via a blank space allocated for this purpose)

```html
<!DOCTYPE html>
<html lang="en">
<head>
<meta charset="utf-8">
<title>Savourly Pouch Label</title>
<link rel="stylesheet" href="https://fonts.googleapis.com/css2?family=Oswald:wght@600&family=Montserrat:wght@700&family=Open+Sans:wght@400;600&display=swap">
<style>
  :root {
    --bg-green: #175a07;
    --leaf-dark: #3f9b3c;
    --leaf-mid: #5cb440;
    --leaf-light: #a8cf45;
    --gold-deep: #d99e2b;
    --gold-light: #f6c452;
    --silver: #e4e6e8;
    --silver-shade: #c9cdd0;
    --cocoa: #4a2a14;
    --tag-green: #3f8f2a;
    --white: #ffffff;
    --window-warm: #b7803f;
    --window-pale: #f3f1ee;
  }
  * { margin: 0; padding: 0; box-sizing: border-box; }
  html, body { width: 1200px; height: 1200px; overflow: hidden; }
  body { background: var(--bg-green); position: relative; font-family: "Open Sans", sans-serif; }

  .pouch {
    position: absolute; left: 330px; top: 110px; width: 540px; height: 980px;
    border-radius: 18px 18px 28px 28px; overflow: hidden; background: var(--window-pale);
  }
  .pouch__top {
    position: absolute; left: 0; top: 0; width: 100%; height: 190px;
    background: linear-gradient(180deg, var(--silver) 0%, #f4f5f6 45%, var(--silver-shade) 100%);
  }
  .pouch__hang-hole {
    position: absolute; left: 50%; top: 38px; width: 70px; height: 22px; margin-left: -35px;
    border-radius: 11px; background: var(--bg-green);
  }
  .pouch__zip { position: absolute; left: 0; top: 130px; width: 100%; height: 6px; background: var(--silver-shade); }

  .label-band {
    position: absolute; left: 0; top: 190px; width: 100%; height: 470px;
    background: linear-gradient(90deg, var(--gold-deep) 0%, var(--gold-light) 50%, var(--gold-deep) 100%);
  }
  .badge { position: absolute; left: 40px; top: 5px; width: 460px; height: 460px; }

  .brand { position: absolute; left: 0; top: 172px; width: 100%; text-align: center;
    font-family: "Oswald", sans-serif; font-weight: 600; font-size: 60px; letter-spacing: 6px; color: var(--cocoa); line-height: 1; }
  .tagline { position: absolute; left: 0; top: 246px; width: 100%; text-align: center;
    font-family: "Montserrat", sans-serif; font-weight: 700; font-size: 11px; letter-spacing: 1px; color: var(--tag-green); text-transform: uppercase; line-height: 1; }
  .packed-by { position: absolute; left: 0; top: 322px; width: 100%; text-align: center; color: var(--tag-green); line-height: 1.35; }
  .packed-by__name { font-weight: 600; font-size: 13px; }
  .packed-by__address { font-size: 10px; }

  .window {
    position: absolute; left: 0; top: 660px; width: 100%; height: 320px;
    background: radial-gradient(ellipse at 50% 40%, var(--window-warm) 0%, #c99a5c 45%, var(--window-pale) 85%);
  }
</style>
</head>
<body>
  <div class="pouch">
    <div class="pouch__top">
      <div class="pouch__hang-hole"></div>
      <div class="pouch__zip"></div>
    </div>

    <div class="label-band">
      <svg class="badge" viewBox="0 0 460 460" aria-hidden="true">
        <g fill="var(--leaf-dark)">
          <rect x="40" y="40" width="380" height="380" rx="90"/>
          <rect x="40" y="40" width="380" height="380" rx="90" transform="rotate(30 230 230)"/>
          <rect x="40" y="40" width="380" height="380" rx="90" transform="rotate(60 230 230)"/>
        </g>
        <g fill="var(--leaf-light)" transform="rotate(15 230 230)">
          <rect x="50" y="50" width="360" height="360" rx="84"/>
          <rect x="50" y="50" width="360" height="360" rx="84" transform="rotate(30 230 230)"/>
          <rect x="50" y="50" width="360" height="360" rx="84" transform="rotate(60 230 230)"/>
        </g>
        <g fill="var(--leaf-mid)" transform="rotate(6 230 230)">
          <rect x="62" y="62" width="336" height="336" rx="80"/>
          <rect x="62" y="62" width="336" height="336" rx="80" transform="rotate(30 230 230)"/>
          <rect x="62" y="62" width="336" height="336" rx="80" transform="rotate(60 230 230)"/>
        </g>
        <circle cx="230" cy="230" r="160" fill="var(--white)"/>
        <circle cx="405" cy="75" r="38" fill="var(--white)" stroke="var(--leaf-mid)" stroke-width="5"/>
        <circle cx="405" cy="75" r="28" fill="none" stroke="var(--leaf-mid)" stroke-width="2"/>
      </svg>
      <div class="brand">SAVOURLY</div>
      <div class="tagline">Taste the goodness in every spoonful!</div>
      <div class="packed-by">
        <div class="packed-by__name">Mwenda Traders Ltd</div>
        <div class="packed-by__address">P. O. Box 41562, Kampala - Uganda</div>
      </div>
    </div>

    <div class="window" role="img" aria-label="See-through window showing the packed food inside the pouch"></div>
  </div>
</body>
</html>
```